K&T Fixit and Rebuild general contracting business card design

I already have a logo that I want to use and I need a card that uses that logo and color scheme on the front with the address phone numbers and email and on the back a place for technicians to write in their name and phone number when they hand it out. It will need the License number of License #KTFXTRB318QN.
It should say General Contractor under the company name. The address is
4417 NE 3rd St, Ste D226
Vancouver, WA 98652
www.kandtfixitandrebuild.example
office@kandtfixitandrebuild.example
360-555-0142 is the telephone number
360-555-0187 is the fax number

Target Market(s)

Homeowners needing remodel work or repairs in their home.

Industry/Entity Type

Construction

Contact Information for Business Card

Business name, address, phone number, license number, fax number, email, and website on the front and a place to fill in technician's name and number

Font styles to use
Serif

Requirements
Must have
• Business name, address, phone number, license number, fax number, email, and website on the front and a place to fill in technician's name and number
Nice to have
• I uploaded an example of a front that is good.
Should not have
• Froo froo or extra embellishments.

```html
<!DOCTYPE html>
<html lang="en">
<head>
<meta charset="utf-8">
<title>K&amp;T Fixit and Rebuild – Business Card</title>
<link rel="stylesheet" href="https://fonts.googleapis.com/css2?family=Exo+2:wght@400;600&family=Michroma&display=swap">
<style>
  :root {
    --page: #e6e8ea;
    --card-top: #83401f;
    --card-bottom: #773819;
    --accent: #ef8a5a;
    --accent-soft: #f2a57c;
    --rule: #f0b08e;
    --field: #f7f7f7;
  }
  * { margin: 0; padding: 0; box-sizing: border-box; }
  html, body { width: 1200px; height: 1200px; overflow: hidden; background: var(--page); }
  body { position: relative; font-family: "Exo 2", sans-serif; color: var(--accent); }

  .card {
    position: absolute;
    left: 262px;
    width: 686px;
    height: 392px;
    background: linear-gradient(180deg, var(--card-top), var(--card-bottom));
  }
  .card--front { top: 165px; }
  .card--back { top: 653px; }

  .brand {
    position: absolute;
    display: flex;
    flex-direction: column;
    align-items: center;
    justify-content: center;
    gap: 6px;
    font-family: "Exo 2", sans-serif;
    font-weight: 600;
    color: var(--accent-soft);
    text-transform: uppercase;
    text-align: center;
  }
  .brand__mark { font-size: 64px; line-height: 1; letter-spacing: 2px; }
  .brand__words { font-size: 17px; letter-spacing: 2px; }
  .card--front .brand { left: 389px; top: 40px; width: 252px; height: 148px; }
  .card--back .brand { left: 52px; top: 125px; width: 218px; height: 132px; }
  .card--back .brand__mark { font-size: 58px; }
  .card--back .brand__words { font-size: 15px; }

  .person { position: absolute; left: 38px; top: 150px; }
  .person__name {
    font-family: "Michroma", sans-serif;
    font-size: 19px;
    letter-spacing: 0.5px;
    color: var(--accent);
    line-height: 1;
  }
  .person__title { font-size: 17px; margin-top: 6px; line-height: 1; }

  .rule {
    position: absolute; left: 38px; top: 204px;
    width: 598px; height: 1px; background: var(--rule);
  }

  .contacts { position: absolute; left: 38px; top: 268px; list-style: none; }
  .contacts li {
    display: flex; align-items: center; gap: 8px;
    font-size: 17px; line-height: 20.5px;
  }
  .contacts svg { width: 14px; height: 14px; fill: var(--accent); flex: none; }

  .address {
    position: absolute; right: 46px; top: 287px;
    text-align: right; font-size: 17px; line-height: 21px;
  }
  .address__license { margin-top: 7px; }

  .fields { position: absolute; left: 305px; top: 133px; width: 321px; }
  .field__label { font-size: 18px; text-transform: uppercase; line-height: 1; letter-spacing: 0.2px; }
  .field__line { height: 23px; background: var(--field); margin-top: 6px; }
  .field + .field { margin-top: 29px; }
</style>
</head>
<body>

<section class="card card--front" aria-label="Business card front">
  <div class="brand">
    <span class="brand__mark">K&amp;T</span>
    <span class="brand__words">Fixit and Rebuild</span>
  </div>

  <div class="person">
    <p class="person__name">DANIEL BROOKS</p>
    <p class="person__title">General Contractor</p>
  </div>

  <div class="rule"></div>

  <ul class="contacts">
    <li>
      <svg viewBox="0 0 16 16" aria-hidden="true"><path d="M3.6 1.2l2.3 2.6-1.3 1.9c.9 2 2.5 3.6 4.6 4.6l1.9-1.3 2.6 2.3-1.2 2.5C7 13.8 2.2 9 1.2 3.1z"/></svg>
      <span>360-555-0142</span>
    </li>
    <li>
      <svg viewBox="0 0 16 16" aria-hidden="true"><path d="M4 1h7l1 1v4H4z M1 7h14v6h-2v-2H3v2H1z M4 12h8v3H4z"/></svg>
      <span>360-555-0187</span>
    </li>
    <li>
      <svg viewBox="0 0 16 16" aria-hidden="true"><path d="M1 3h14v1.5L8 9 1 4.5z M1 6.3l7 4.5 7-4.5V13H1z"/></svg>
      <span>office@kandtfixitandrebuild.example</span>
    </li>
    <li>
      <svg viewBox="0 0 16 16" aria-hidden="true"><circle cx="8" cy="8" r="7"/></svg>
      <span>kandtfixitandrebuild.example</span>
    </li>
  </ul>

  <div class="address">
    <p>4417 NE 3rd St, Ste D226</p>
    <p>Vancouver, WA 98652</p>
    <p class="address__license">Lic No: #KTFXTRB318QN.</p>
  </div>
</section>

<section class="card card--back" aria-label="Business card back">
  <div class="brand">
    <span class="brand__mark">K&amp;T</span>
    <span class="brand__words">Fixit and Rebuild</span>
  </div>

  <div class="fields">
    <div class="field">
      <p class="field__label">Technician's Name</p>
      <div class="field__line"></div>
    </div>
    <div class="field">
      <p class="field__label">Phone Number</p>
      <div class="field__line"></div>
    </div>
  </div>
</section>

</body>
</html>
```